New Business Card Design Project

Looking for a modern business card design for an import distribution business for industrial technical products. The winning design will translate modern, sophistication, technical, professional and sustainable.

Target Market(s)

Technical customers

Industry/Entity Type

Business

Contact Information for Business Card

Dean Harlow
Sales Manager
M: 0471 625 183
P: 1300 872 619
dean@volkarsystems.com.au
4/18 Galloway Crest Road
Brennock Vale NSW 2147
www.volkarsystems.com.au

Font styles to use
Sans Serif

Colors
ec1f27
606060
000000
fbfbfb

Requirements
Must have
• My Logo which is the Volkar Systems logo attached
Nice to have
• Eurostile Bold font

```html
<!DOCTYPE html>
<html lang="en">
<head>
<meta charset="utf-8">
<title>Volkar Systems – Business Card</title>
<link rel="stylesheet" href="https://fonts.googleapis.com/css2?family=Michroma&family=Saira:wght@500;600&display=swap">
<style>
  :root {
    --brand-red: #ec1f27;
    --brand-grey: #606060;
    --ink: #000000;
    --card-white: #fbfbfb;
    --backdrop: #bfe3da;
    --font-display: "Michroma", sans-serif;
    --font-body: "Saira", sans-serif;
  }
  * { box-sizing: border-box; margin: 0; padding: 0; }
  html, body { width: 1200px; height: 856px; overflow: hidden; }
  body { background: var(--backdrop); position: relative; font-family: var(--font-body); }

  .card {
    position: absolute;
    width: 520px; height: 318px;
    background: var(--card-white);
    border-radius: 22px;
    overflow: hidden;
    box-shadow: 0 6px 18px rgba(0,0,0,0.12);
  }
  .card--back { left: 610px; top: 70px; }
  .card--front { left: 70px; top: 440px; }

  /* Back */
  .back-brand {
    position: absolute; left: 0; right: 0; top: 104px;
    display: flex; align-items: center; justify-content: center; gap: 16px;
  }
  .brand-square { width: 34px; height: 34px; background: var(--brand-red); flex: none; }
  .back-brand .brand-name {
    font-family: var(--font-display); font-size: 28px; color: var(--brand-red); white-space: nowrap;
  }
  .back-web {
    position: absolute; left: 0; right: 0; bottom: 36px; text-align: center;
    font-family: var(--font-body); font-weight: 600; font-size: 15px; color: var(--brand-grey);
  }

  /* Front */
  .front-band { position: absolute; inset: 0; }
  .front-brand {
    position: absolute; left: 34px; top: 34px;
    display: flex; align-items: center; gap: 14px;
  }
  .front-brand .brand-square { width: 38px; height: 38px; }
  .front-brand .brand-name {
    font-family: var(--font-display); font-size: 28px; color: var(--brand-red); white-space: nowrap;
  }
  .person { position: absolute; left: 150px; top: 98px; }
  .person__name {
    font-family: var(--font-display); font-size: 22px; color: var(--ink); letter-spacing: 0.5px;
    white-space: nowrap;
  }
  .person__role {
    font-family: var(--font-body); font-weight: 600; font-size: 15px; color: var(--brand-grey);
    margin-left: 70px; margin-top: 2px;
  }
  .phones {
    position: absolute; left: 36px; top: 178px;
    display: flex; flex-direction: column; gap: 8px;
  }
  .contact-line {
    display: flex; align-items: center; gap: 10px; line-height: 26px;
    font-family: var(--font-body); font-weight: 600; font-size: 19px; color: var(--card-white);
    letter-spacing: 0.5px; white-space: nowrap;
  }
  .icon-dot {
    width: 22px; height: 22px; border-radius: 50%; background: var(--card-white); flex: none;
    display: flex; align-items: center; justify-content: center;
  }
  .address {
    position: absolute; left: 292px; top: 170px;
    font-family: var(--font-body); font-weight: 600; font-size: 15px; line-height: 1.3;
    color: var(--card-white); white-space: nowrap;
  }
  .online {
    position: absolute; left: 256px; top: 236px;
    display: flex; flex-direction: column; gap: 3px;
  }
  .online__web {
    font-family: var(--font-body); font-weight: 600; font-size: 14px; color: var(--brand-grey);
    margin-left: 30px; white-space: nowrap;
  }
  .online__email {
    display: flex; align-items: center; gap: 8px; white-space: nowrap;
    font-family: var(--font-body); font-weight: 600; font-size: 15px; color: var(--brand-grey);
  }
  .online__email .icon-dot { background: var(--brand-red); }
</style>
</head>
<body>

  <section class="card card--back" aria-label="Business card back">
    <div class="back-brand">
      <span class="brand-square"></span>
      <span class="brand-name">VOLKAR SYSTEMS</span>
    </div>
    <p class="back-web">www.volkarsystems.com.au</p>
  </section>

  <section class="card card--front" aria-label="Business card front">
    <svg class="front-band" width="520" height="318" viewBox="0 0 520 318" aria-hidden="true">
      <polygon points="0,160 520,160 520,228 260,228 240,290 0,290" fill="var(--brand-red)"/>
      <polygon points="506,228 514,228 494,290 486,290" fill="var(--brand-red)"/>
    </svg>

    <div class="front-brand">
      <span class="brand-square"></span>
      <span class="brand-name">VOLKAR SYSTEMS</span>
    </div>

    <div class="person">
      <p class="person__name">DEAN HARLOW</p>
      <p class="person__role">Sales Manager</p>
    </div>

    <div class="phones">
      <p class="contact-line">
        <span class="icon-dot">
          <svg width="10" height="14" viewBox="0 0 10 14" aria-hidden="true">
            <rect x="1" y="1" width="8" height="12" rx="1.5" fill="none" stroke="var(--brand-red)" stroke-width="1.6"/>
            <circle cx="5" cy="10.5" r="0.9" fill="var(--brand-red)"/>
          </svg>
        </span>
        0471 625 183
      </p>
      <p class="contact-line">
        <span class="icon-dot">
          <svg width="13" height="13" viewBox="0 0 24 24" aria-hidden="true">
            <path d="M6.6 10.8a15.1 15.1 0 0 0 6.6 6.6l2.2-2.2a1 1 0 0 1 1-.25 11.4 11.4 0 0 0 3.6.57 1 1 0 0 1 1 1V20a1 1 0 0 1-1 1A17 17 0 0 1 3 4a1 1 0 0 1 1-1h3.5a1 1 0 0 1 1 1c0 1.25.2 2.450.57 3.57a1 1 0 0 1-.25 1z" fill="var(--brand-red)"/>
          </svg>
        </span>
        1300 872 619
      </p>
    </div>

    <p class="address">4/18 Galloway Crest Road<br>Brennock Vale NSW</p>

    <div class="online">
      <p class="online__web">www.volkarsystems.com.au</p>
      <p class="online__email">
        <span class="icon-dot">
          <svg width="12" height="9" viewBox="0 0 12 9" aria-hidden="true">
            <rect x="0.5" y="0.5" width="11" height="8" fill="none" stroke="var(--card-white)" stroke-width="1.2"/>
            <polyline points="0.5,0.5 6,5 11.5,0.5" fill="none" stroke="var(--card-white)" stroke-width="1.2"/>
          </svg>
        </span>
        dean@volkarsystems.com.au
      </p>
    </div>
  </section>

</body>
</html>
```